New Business Card Design Project

Updated business card design. I am moving towards more coaching of, for the most part women, who are searching for more in their lives. I am an intuitive healer, homeopath and nutritionist but also an author and motivational speaker. Int the past I have included my photo on the card but that is not essential. My book is called the Brilliance of Saffron - Reclaiming the Shade of Your Spirit so my colours are typically magenta.
Target Market(s)
Women - 35 - 60 considering improving their health. However, I am also a professional speaker with a target audience including corporate and conferences.
Industry/Entity Type
Health And Wellness
Contact Information for Business Card
Lucinda Parvell, CNP, MA
www.lucindaparvell.com
lucinda@lucindaparvell.com
519-362-7015
Facebook, instagram and twitter logos
Look and feel
Each slider illustrates characteristics of the customer's brand and the style your logo design should communicate.

```html
<!DOCTYPE html>
<html lang="en">
<head>
<meta charset="utf-8">
<title>Lucinda Parvell – Business Card</title>
<link rel="stylesheet" href="https://fonts.googleapis.com/css2?family=Italiana&family=Poppins:wght@300;400;500&display=swap">
<style>
  :root {
    --backdrop: #2b2d31;
    --marble-light: #ffffff;
    --marble-mid: #ecebee;
    --marble-vein: #dcdbe0;
    --magenta: #e6237a;
    --ink: #1c1c1e;
    --ink-soft: #3a3a3e;
    --tagline: #6d6d72;
  }
  * { box-sizing: border-box; margin: 0; padding: 0; }
  html, body {
    width: 1200px; height: 900px; overflow: hidden;
    background: var(--backdrop);
  }
  .sheet {
    width: 1200px; height: 900px;
    display: flex; flex-direction: column;
    align-items: center; justify-content: center; gap: 56px;
  }
  .card {
    position: relative;
    width: 640px; height: 366px;
    border-radius: 22px;
    overflow: hidden;
  }
  .card__marble {
    position: absolute; inset: 0;
    background:
      radial-gradient(ellipse at 30% 25%, var(--marble-light) 0%, transparent 60%),
      radial-gradient(ellipse at 75% 80%, var(--marble-vein) 0%, transparent 55%),
      linear-gradient(135deg, var(--marble-light) 0%, var(--marble-mid) 55%, var(--marble-light) 100%);
  }

  /* brand block */
  .brand {
    position: relative;
    display: flex; flex-direction: column;
  }
  .brand__name {
    font-family: "Italiana", serif;
    color: var(--ink);
    line-height: 1;
  }
  .brand__line { display: flex; align-items: center; }
  .brand__line--second { padding-left: 1.1em; }
  .brand__dot {
    border-radius: 50%;
    background: var(--magenta);
    flex: none;
  }
  .brand__tagline {
    display: flex; align-items: center;
    font-family: "Poppins", sans-serif;
    font-weight: 300;
    color: var(--tagline);
    letter-spacing: 0.04em;
  }
  .brand__tagline::before,
  .brand__tagline::after {
    content: ""; width: 6px; height: 6px; border-radius: 50%;
    background: var(--magenta); flex: none;
  }
  .brand__tagline::before { margin-right: 10px; }
  .brand__tagline::after { margin-left: 10px; }

  /* front */
  .card--front .brand {
    height: 100%; justify-content: center; align-items: center;
  }
  .card--front .brand__name { font-size: 72px; }
  .card--front .brand__line { gap: 14px; }
  .card--front .brand__dot { width: 52px; height: 52px; }
  .card--front .brand__tagline { font-size: 24px; margin-top: 16px; padding-left: 60px; }

  /* back */
  .card--back .card__band {
    position: absolute; top: 0; right: 0; bottom: 0;
    width: 34px; background: var(--magenta);
  }
  .card--back .card__content {
    position: absolute; left: 46px; top: 28px; right: 110px;
  }
  .card--back .brand__name { font-size: 44px; }
  .card--back .brand__line { gap: 10px; }
  .card--back .brand__dot { width: 32px; height: 32px; }
  .card--back .brand__tagline { font-size: 15px; margin-top: 6px; }

  .holder {
    margin-top: 16px;
    font-family: "Poppins", sans-serif;
    font-weight: 500; font-size: 18px;
    color: var(--ink);
  }
  .contact-list {
    list-style: none; margin-top: 10px;
    font-family: "Poppins", sans-serif;
    font-weight: 400; font-size: 14px;
    color: var(--ink-soft);
  }
  .contact-list li {
    display: flex; align-items: center; gap: 12px;
    margin-bottom: 6px;
  }
  .contact-list svg { width: 16px; height: 16px; flex: none; }

  .social {
    position: absolute; right: 50px; top: 50%;
    transform: translateY(-50%);
    display: flex; flex-direction: column; gap: 18px;
  }
  .social__item {
    width: 40px; height: 40px; border-radius: 50%;
    border: 2px solid var(--magenta);
    background: var(--marble-light);
  }
</style>
</head>
<body>
<main class="sheet">

  <section class="card card--front" aria-label="Business card front">
    <div class="card__marble" role="img" aria-label="White marble texture with soft grey veins"></div>
    <div class="brand">
      <div class="brand__name">
        <div class="brand__line">Lucinda <span class="brand__dot"></span></div>
        <div class="brand__line brand__line--second">Parvell</div>
      </div>
      <div class="brand__tagline">vitality maverick</div>
    </div>
  </section>

  <section class="card card--back" aria-label="Business card back">
    <div class="card__marble" role="img" aria-label="White marble texture with soft grey veins"></div>
    <div class="card__band"></div>

    <div class="card__content">
      <div class="brand">
        <div class="brand__name">
          <div class="brand__line">Lucinda <span class="brand__dot"></span></div>
          <div class="brand__line brand__line--second">Parvell</div>
        </div>
        <div class="brand__tagline">vitality maverick</div>
      </div>

      <p class="holder">Lucinda Parvell, CNP, MA</p>

      <ul class="contact-list">
        <li>
          <svg viewBox="0 0 16 16" aria-hidden="true">
            <rect width="16" height="16" rx="3" fill="#e6237a"/>
            <path d="M5 3.5c.6 0 1 .9 1.3 1.6.2.5-.5 1-.6 1.3.5 1.2 1.4 2.2 2.6 2.7.3-.1.8-.8 1.3-.6.7.3 1.6.7 1.6 1.3 0 .9-1 1.7-1.9 1.6C6 11 4.9 8 4 6 3.7 5 4 3.5 5 3.5z" fill="#fff"/>
          </svg>
          519-362-7015
        </li>
        <li>
          <svg viewBox="0 0 16 16" aria-hidden="true">
            <rect width="16" height="16" rx="3" fill="#e6237a"/>
            <rect x="3" y="4.5" width="10" height="7" fill="none" stroke="#fff" stroke-width="1.2"/>
            <path d="M3 4.5l5 4 5-4" fill="none" stroke="#fff" stroke-width="1.2"/>
          </svg>
          lucinda@lucindaparvell.com
        </li>
        <li>
          <svg viewBox="0 0 16 16" aria-hidden="true">
            <rect width="16" height="16" rx="3" fill="#e6237a"/>
            <circle cx="8" cy="8" r="5" fill="none" stroke="#fff" stroke-width="1.1"/>
            <ellipse cx="8" cy="8" rx="2.2" ry="5" fill="none" stroke="#fff" stroke-width="1"/>
            <path d="M3 8h10" stroke="#fff" stroke-width="1"/>
          </svg>
          www.lucindaparvell.com
        </li>
      </ul>
    </div>

    <div class="social" aria-label="Social media">
      <span class="social__item"></span>
      <span class="social__item"></span>
      <span class="social__item"></span>
    </div>
  </section>

</main>
</body>
</html>
```